Flyer, poster, banner and social media titles designs for Community Renewal Guidlines

The Shared Guidelines for Community Renewal provide a nationally agreed framework to guide recovery policy and practice across Australia. The Principles support recovery practitioners, governments, non-government organisations and communities to deliver effective, community-centred recovery outcomes.
The Principles have recently been refreshed through extensive consultation and we require a contemporary visual identity and design suite that will increase awareness, engagement and practical application of the Principles.
The redesign will cover:
• A4 Brochure (primary publication)
• A3 Poster
• Pull up banner
• Social Media Tiles
The new design should:
• Create a recognisable brand for the Shared Guidelines.
• Appeal to both experienced and emerging recovery practitioners.
• Reflect contemporary disaster recovery practice.
• Feel people-focused rather than government-focused.
• Support future resources such as videos, implementation guides, presentations and workshop materials.
• Remain relevant for several years without requiring a major redesign.
Target Audience
• Disaster recovery practitioners
• Government agencies
• Non-government organisations
• Community recovery workers
• Recovery managers and leaders
• Community stakeholders and volunteers
The visual identity should reflect the six Principles:
• Understanding Context
• Recognising Complexity
• Community-Centred Approaches
• Coordination
• Communication
• Capacity Building
The design should communicate:
• Recovery is centred on people and communities.
• Recovery is collaborative and involves many sectors.
• Recovery is adaptive, inclusive and evidence-informed.
• Recovery supports resilience and long-term wellbeing.
• The Principles provide practical guidance for recovery practice.
We are looking for:
• Modern and professional
• Warm and approachable
• Human-centred
• Inclusive and accessible
• Australian in context
• Visually engaging
• Suitable for print and digital use
We would like to avoid:
• Images of disaster destruction
• Emergency response imagery (fire trucks, flashing lights, etc.)
• Overly corporate or bureaucratic designs
• Designs that focus on deficits rather than recovery and growth
Consider themes such as:
• Connection and collaboration
• Communities and people
• Growth, recovery and renewal
Accessibility
Designs should:
• Meet accessibility best practice
• Use clear typography
• Achieve strong colour contrast
• Be suitable for both digital and print formats

Deliverables
1. Principles Brochure
• A4 trifold size x 2 (online and print friendly version)
• A side to include cover side, logos side and overview of principles.
• B side full details of the principles
• Graphic to highlight the 3 c’s concept (RECOVERY Context, complexity, community centred, coordinate, communicate and capacity). Currently 3 circles.
• Can be printed and distributed electronically
2. Poster
• A1 and A3 versions
• Suitable for office and workshop display
3. Pull-Up Banner - 850 mm (W) × 2000 mm (H)
• Conference and event use
• High visual impact
• Strong branding and concise messaging
4. Social Media Tiles x 3
Updates

We are providing an extension and increasing the budget following feedback from designers. We are wanting the resources to look and feel different from the existing designs, considering either a different colour palette in the designs or different motif with the leave design. Any nature based designs should consider the Australian fauna or flora. Also suggest avoiding images in the designs. The principles are not numbered or liner in the concept of how they function. Happy to answer any further questions and thank you for your suggested concepts.

Target Market(s)

Disaster recovery practitioners, Government agencies , Non-government organisations, Community recovery workers and Community stakeholders and volunteers

Industry/Entity Type

Disaster recovery

Colors

Designer to choose colors to be used in the design.

Requirements
Must have
• Modern, warm, visually engaging, human-centred, Australian in context and different to the current design.
Nice to have
• Symbols for each principles
Should not have
• Images of disaster destruction, Emergency response imagery, Overly corporate or bureaucratic designs, Designs that focus on deficits rather than recovery and growth, avoid too much black

```html
<!DOCTYPE html>
<html lang="en">
<head>
<meta charset="utf-8">
<title>Shared Guidelines for Community Renewal – Trifold Brochure</title>
<link href="https://fonts.googleapis.com/css2?family=Open+Sans:wght@400;600&family=Poppins:wght@400;500;600&display=swap" rel="stylesheet">
<style>
:root{
  --green:#6a9e34;
  --green-soft:#8dbb52;
  --charcoal:#404042;
  --mist:#e9e9eb;
  --paper:#ffffff;
  --backdrop:#9c9c9c;
  --ink:#3b3b3d;
  --ink-soft:#555558;
}
*{box-sizing:border-box;margin:0;padding:0}
html,body{width:1200px;height:2501px;overflow:hidden}
body{background:var(--backdrop);font-family:"Open Sans",Arial,sans-serif;color:var(--ink);position:relative}
.spread{position:absolute;left:20px;width:1160px;height:900px;display:flex;box-shadow:0 4px 18px rgba(0,0,0,.25)}
.spread--front{top:325px}
.spread--back{top:1275px}
.panel{position:relative;width:386.67px;height:100%;overflow:hidden}
.panel--dark{background:var(--charcoal);color:#fff}
.panel--mist{background:var(--mist)}
.panel--paper{background:var(--paper)}

/* flat artwork areas */
.art{position:absolute;border-radius:4px}
.art--green{background:linear-gradient(160deg,rgba(141,187,82,.55),rgba(106,158,52,.55))}
.art--dark{background:linear-gradient(160deg,rgba(64,64,66,.35),rgba(44,44,46,.35))}
.art--faint-light{background:linear-gradient(160deg,rgba(255,255,255,.07),rgba(255,255,255,.03))}
.art--faint-dark{background:linear-gradient(160deg,rgba(0,0,0,.05),rgba(0,0,0,.02))}

/* Front intro panel */
.intro{position:relative;padding:28px 24px 0 26px}
.kicker{font-size:11px;letter-spacing:.02em;text-transform:uppercase}
.title-word{display:block;font-family:"Open Sans",sans-serif;font-weight:400;line-height:.95;letter-spacing:-.01em}
.intro .title-word{font-size:40px}
.title-word--green{color:var(--green)}
.intro p{font-size:10.3px;line-height:1.3;margin-top:12px;color:#f1f1f1}
.intro .title-block + p{margin-top:22px}
.pill{display:inline-block;margin-top:13px;background:var(--green);color:#fff;font-family:"Poppins",sans-serif;font-size:10.5px;padding:3px 12px;border-radius:12px}
.intro .lead{font-size:11.2px;margin-top:8px}
.section-title{font-family:"Poppins",sans-serif;font-size:14px;font-weight:500;margin-top:18px;letter-spacing:.02em}
.principle-grid{display:grid;grid-template-columns:1fr 1fr;column-gap:18px;margin-top:14px}
.principle-card{padding:6px 0 10px;border-top:1px solid rgba(255,255,255,.22);font-size:9.6px;line-height:1.28}
.principle-card:nth-child(-n+2){border-top:none;padding-top:0}
.principle-card:nth-child(odd){border-right:1px solid rgba(255,255,255,.22);padding-right:10px}
.principle-card h4{font-family:"Poppins",sans-serif;font-weight:500;font-size:9.6px;color:var(--green-soft);line-height:1.2}
.cycle-badge{position:absolute;left:290px;bottom:26px}

/* Partners panel */
.partners{display:grid;grid-template-columns:1fr 1fr;gap:20px 10px;padding:130px 30px 0}
.partner{display:flex;flex-direction:column;align-items:center;text-align:center;gap:6px;min-height:70px;justify-content:center}
.partner-dot{width:34px;height:34px;border-radius:50%;background:#cfcfd2}
.partner-name{font-size:9.6px;font-weight:600;color:var(--ink);line-height:1.2}
.partners-caption{text-align:center;font-size:10.5px;color:var(--ink-soft);margin-top:26px;letter-spacing:.02em}
.partner--lead{flex-direction:row;justify-content:center;margin-top:14px;gap:10px;min-height:0}
.partner--lead .partner-name{text-align:left;font-size:10.5px;font-weight:600}

/* Cover panel */
.cover-title{position:absolute;left:40px;top:56px}
.cover-title .kicker{font-size:14px}
.cover-title .title-word{font-size:58px;margin-top:2px}
.ground-edge{position:absolute;left:0;width:100%;display:block}
.cover-ground{position:absolute;left:0;right:0;bottom:0;height:340px;background:var(--charcoal)}
.cover-message{position:absolute;left:40px;top:590px;width:300px}
.cover-message h2{font-family:"Poppins",sans-serif;font-weight:500;font-size:17px;line-height:1.2;color:var(--green-soft)}
.cover-message p{font-size:14.5px;line-height:1.35;margin-top:12px;color:#f1f1f1}

/* Back spread */
.principle{position:absolute;left:0;right:0;padding:0 26px}
.principle--top{top:0;height:400px;padding-top:24px}
.principle--base{top:400px;bottom:0;padding-top:46px;color:#fff}
.principle h3{font-family:"Poppins",sans-serif;font-weight:500;font-size:16.5px;line-height:1.2;color:var(--green)}
.principle--base h3{color:var(--green-soft)}
.principle--base.is-green h3{color:#fff}
.principle .summary{font-size:9.6px;line-height:1.28;margin-top:14px}
.principle--base .summary{margin-top:10px}
.checklist{list-style:none;margin-top:10px;padding-left:20px}
.checklist li{position:relative;font-size:9.5px;line-height:1.25;margin-bottom:4px}
.checklist li::before{content:"";position:absolute;left:-15px;top:3px;border-left:6px solid var(--green);border-top:4px solid transparent;border-bottom:4px solid transparent}
.principle--base .checklist li::before{border-left-color:var(--green-soft)}
.principle--base.is-green .checklist li::before{border-left-color:#fff}
.base-fill{position:absolute;left:0;right:0;top:400px;bottom:0}
.base-fill--dark{background:var(--charcoal)}
.base-fill--green{background:var(--green)}
</style>
</head>
<body>

<section class="spread spread--front" aria-label="Brochure outer side">
  <article class="panel panel--dark">
    <div class="art art--green" style="left:232px;top:46px;width:76px;height:48px" role="img" aria-label="Green leaf sprig illustration"></div>
    <div class="intro">
      <div class="title-block">
        <div class="kicker">Shared Guidelines for</div>
        <span class="title-word">Community</span>
        <span class="title-word title-word--green">Renewal</span>
      </div>
      <p>Disasters can deeply impact lives and livelihoods. Working with communities recovering from disasters is complex and challenging. Recovery is long-term, non-linear and dynamic, particularly in the context of compounding and concurrent disasters. These principles are a way to guide our efforts, our approach, our planning and our decision-making.</p>
      <p>Disaster recovery is part of emergency management, which includes the broader components of prevention, preparedness and response. Planning for recovery is integral to emergency preparation, and mitigation actions are often initiated as part of recovery.</p>
      <p>Disaster recovery includes built, environmental and economic elements, as well as individual and social wellbeing. Recovery can provide an opportunity to improve these aspects beyond previous conditions, by enhancing social and natural environments, infrastructure and economies – contributing to more resilient communities.</p>
      <span class="pill">The Relationship Between The Principles</span>
      <p class="lead">While all the principles are equally critical to ensure effective recovery, understanding the local and broader context and recognising complexity are foundational. The descriptions beneath each principle provide further guidance for working with communities in disaster recovery.</p>
      <h2 class="section-title">SUCCESSFUL RECOVERY</h2>
      <div class="principle-grid">
        <div class="principle-card"><h4>Understand the CONTEXT</h4>Successful recovery is based on an understanding of the community context, with each community having its own history, values and dynamics.</div>
        <div class="principle-card"><h4>COORDINATE all activities</h4>Successful recovery requires a planned, coordinated and adaptive approach, between community and partner agencies, based on continuing assessment of impacts and needs.</div>
        <div class="principle-card"><h4>Recognise COMPLEXITY</h4>Successful recovery is responsive to the complex and evolving nature of disasters and their impacts on communities, including compounding, cascading and concurrent events.</div>
        <div class="principle-card"><h4>COMMUNICATE effectively</h4>Successful recovery is built on effective communication between the affected community and other partners.</div>
        <div class="principle-card"><h4>Use COMMUNITY-CENTRED approaches</h4>Successful recovery is community-centred, responsive and flexible, engaging with community and supporting them to move forward, with shared responsibilities.</div>
        <div class="principle-card"><h4>Recognise and build CAPACITY</h4>Successful recovery recognises, supports and builds on individual, community and organisational capacity and resilience.</div>
      </div>
    </div>
    <svg class="cycle-badge" width="76" height="76" viewBox="0 0 76 76" aria-label="Recovery principles cycle">
      <circle cx="38" cy="38" r="36" fill="none" stroke="#6b6b6e" stroke-width="1.5"/>
      <circle cx="38" cy="38" r="27" fill="none" stroke="#6b6b6e" stroke-width="1"/>
      <circle cx="38" cy="38" r="17" fill="#6a9e34"/>
      <text x="38" y="40.5" text-anchor="middle" font-family="Poppins, sans-serif" font-size="6.5" fill="#fff">RECOVERY</text>
    </svg>
  </article>

  <article class="panel panel--mist">
    <div class="art art--dark" style="left:290px;top:0;width:80px;height:70px" role="img" aria-label="Dark leaf sprig illustration"></div>
    <div class="partners">
      <div class="partner"><span class="partner-dot"></span><span class="partner-name">Federal Office of<br>Community Services</span></div>
      <div class="partner"><span class="partner-dot"></span><span class="partner-name">Federal Office of<br>Civic Affairs</span></div>
      <div class="partner"><span class="partner-dot"></span><span class="partner-name">Harbour Aid Society</span></div>
      <div class="partner"><span class="partner-dot"></span><span class="partner-name">Southern Region<br>Government</span></div>
      <div class="partner"><span class="partner-dot"></span><span class="partner-name">Western Region<br>Government</span></div>
      <div class="partner"><span class="partner-dot"></span><span class="partner-name">Island State<br>Government</span></div>
      <div class="partner"><span class="partner-dot"></span><span class="partner-name">Northeast Region<br>Government</span></div>
      <div class="partner"><span class="partner-dot"></span><span class="partner-name">Capital District<br>Government</span></div>
      <div class="partner"><span class="partner-dot"></span><span class="partner-name">Top End Region<br>Government</span></div>
      <div class="partner"><span class="partner-dot"></span><span class="partner-name">Southeast State<br>Government</span></div>
      <div class="partner"><span class="partner-dot"></span><span class="partner-name">Coastal State Office of<br>Emergency Planning</span></div>
      <div class="partner"></div>
    </div>
    <p class="partners-caption">PARTNERS IN DEVELOPMENT FROM THE</p>
    <div class="partner partner--lead"><span class="partner-dot"></span><span class="partner-name">Community Renewal<br>Advisory Circle</span></div>
    <div class="art art--green" style="left:0;top:800px;width:80px;height:70px" role="img" aria-label="Green leaf sprig illustration"></div>
  </article>

  <article class="panel panel--paper">
    <div class="art art--faint-dark" style="left:200px;top:340px;width:180px;height:190px" role="img" aria-label="Faint grass and leaf line illustration"></div>
    <div class="art art--green" style="left:250px;top:225px;width:110px;height:80px" role="img" aria-label="Green leaf sprig illustration"></div>
    <div class="art art--green" style="left:30px;top:410px;width:80px;height:90px" role="img" aria-label="Green seedling illustration"></div>
    <div class="cover-title">
      <div class="kicker">Shared Guidelines for</div>
      <span class="title-word">Community</span>
      <span class="title-word title-word--green">Renewal</span>
    </div>
    <div class="cover-ground"></div>
    <svg class="ground-edge" style="top:536px" height="30" viewBox="0 0 387 30" preserveAspectRatio="none" aria-hidden="true">
      <path d="M0 18 C30 8 55 22 90 12 S150 4 190 14 S260 22 300 10 S360 6 387 14 L387 30 L0 30Z" fill="#404042"/>
    </svg>
    <div class="art art--faint-light" style="left:250px;top:760px;width:110px;height:100px" role="img" aria-label="Faint leaf illustration"></div>
    <div class="cover-message">
      <h2>Disasters can deeply impact lives and livelihoods.</h2>
      <p>Working with communities recovering from disasters is complex and challenging.</p>
    </div>
  </article>
</section>

<section class="spread spread--back" aria-label="Brochure inner side">
  <article class="panel panel--paper">
    <div class="art art--dark" style="left:60px;top:330px;width:60px;height:50px" role="img" aria-label="Dark seedling illustration"></div>
    <div class="principle principle--top">
      <h3>Understand the CONTEXT:</h3>
      <p class="summary">Successful recovery is based on an understanding of the community context, with each community having its own history, values and dynamics. Recovery should:</p>
      <ul class="checklist">
        <li>Acknowledge existing strengths and capacity, including past experiences and future aspirations;</li>
        <li>Appreciate the risks and stressors faced by the community;</li>
        <li>Embed accessibility, equity, inclusion and diversity in recovery practice, using culturally safe and trauma-informed approaches;</li>
        <li>Support people who may be at greater risk or disproportionately impacted;</li>
        <li>Respect and support connections to Country, environment, animals and culturally significant places and recognise environmental regeneration in recovery;</li>
        <li>Recognise pathways and timeframes vary; systems should support long-term recovery shaped by community needs; and</li>
        <li>Acknowledge the impact upon the community may extend beyond the geographical boundaries where the disaster occurred.</li>
      </ul>
    </div>
    <div class="base-fill base-fill--dark"></div>
    <svg class="ground-edge" style="top:376px" height="26" viewBox="0 0 387 26" preserveAspectRatio="none" aria-hidden="true"><path d="M0 14 C40 6 70 20 110 10 S170 2 220 12 S300 20 340 8 S375 10 387 12 L387 26 L0 26Z" fill="#404042"/></svg>
    <div class="principle principle--base">
      <h3>Recognise COMPLEXITY</h3>
      <p class="summary">Successful recovery is responsive to the complex and evolving nature of disasters and their impacts on communities, including compounding, cascading and concurrent events. Recovery should recognise that:</p>
      <ul class="checklist">
        <li>Disasters lead to a range of effects and impacts that require a variety of approaches; they can also leave long-term legacies;</li>
        <li>Information on impacts and needs can be limited at first and changes over time;</li>
        <li>Affected individuals and the community have diverse needs, wants and expectations, which can evolve rapidly;</li>
        <li>Responsive and flexible action is crucial to addressing immediate needs;</li>
        <li>Existing community knowledge and values may challenge the assumptions of those outside of the community;</li>
        <li>Conflicting knowledge, values and priorities among individuals, the community and organisations may create tensions;</li>
        <li>Emergencies create stressful environments where grief or blame may also affect those involved; and</li>
        <li>Over time, appropriate support for individuals and communities, from within and outside, can cultivate hope and individual and collective growth.</li>
      </ul>
    </div>
  </article>

  <article class="panel panel--mist">
    <div class="principle principle--top">
      <h3>Use COMMUNITY-CENTRED approaches:</h3>
      <p class="summary">Successful recovery is community-centred, responsive and flexible, engaging with community and supporting them to move forward, with shared responsibilities. Recovery should:</p>
      <ul class="checklist">
        <li>Assist and enable individuals, families and the community to actively participate in their own recovery;</li>
        <li>Recognise that individuals and the community may need different levels of support at various times;</li>
        <li>Be guided by the communities' priorities;</li>
        <li>Channel effort through pre-identified and existing community assets, including local knowledge, existing community strengths and resilience;</li>
        <li>Build collaborative partnerships that reflect diverse representation and community leadership in recovery;</li>
        <li>Support Aboriginal and Torres Strait Islander self-determination and Indigenous governance, recognising Country as central to recovery and resilience;</li>
        <li>Recognise that new community leaders often emerge during and after a disaster, who may not hold formal positions of authority; and</li>
        <li>Recognise that different communities may choose different paths to recovery.</li>
      </ul>
    </div>
    <div class="base-fill base-fill--green"></div>
    <svg class="ground-edge" style="top:376px" height="26" viewBox="0 0 387 26" preserveAspectRatio="none" aria-hidden="true"><path d="M0 10 C30 18 80 4 120 14 S200 20 240 8 S320 4 350 14 S380 12 387 10 L387 26 L0 26Z" fill="#6a9e34"/></svg>
    <div class="principle principle--base is-green">
      <h3>COORDINATE all activities:</h3>
      <p class="summary">Successful recovery requires a planned, coordinated and adaptive approach, between community and partner agencies, based on continuing assessment of impacts and need. Recovery should:</p>
      <ul class="checklist">
        <li>Have clearly articulated and shared goals based on desired outcomes;</li>
        <li>Be flexible, taking into account changes in community needs or stakeholder expectations;</li>
        <li>Be guided by those with experience and expertise, using skilled, authentic and capable community leadership;</li>
        <li>Be at the pace desired by the community, and seek to collaborate and reconcile different interests and time frames;</li>
        <li>Reflect well-developed community planning and information gathering before, during and after a disaster;</li>
        <li>Have clear decision-making and reporting structures and sound governance, which are transparent and accessible to the community;</li>
        <li>Demonstrate an understanding of the roles, responsibilities and authority of organisations involved and coordinate across agencies to ensure minimal service provision disruption;</li>
        <li>Be part of an emergency management approach that integrates with response operations and contributes to future prevention and preparedness; and</li>
        <li>Be inclusive, availing of and building upon relationships created before, during and after the emergency.</li>
      </ul>
    </div>
  </article>

  <article class="panel panel--paper">
    <div class="art art--dark" style="left:190px;top:320px;width:56px;height:60px" role="img" aria-label="Dark seedling illustration"></div>
    <div class="principle principle--top">
      <h3>COMMUNICATE<br>effectively:</h3>
      <p class="summary">Successful recovery is built on effective communication between the affected community and other partners. Recovery should:</p>
      <ul class="checklist">
        <li>Recognise that communication should be two-way, transparent and ongoing, building trust through shared understanding and feedback;</li>
        <li>Ensure that information is accessible to audiences in diverse situations, addresses a variety of communication needs, and is provided through a range of communication channels and networks;</li>
        <li>Establish mechanisms for coordinated and consistent communications between all service providers, organisations and individuals and the community;</li>
        <li>Ensure that all communication is relevant, timely, clear, accurate, targeted, credible and consistent; and</li>
        <li>Identify trusted sources of information and repeat key recovery messages to enable greater community confidence and receptivity.</li>
      </ul>
    </div>
    <div class="base-fill base-fill--dark"></div>
    <svg class="ground-edge" style="top:376px" height="26" viewBox="0 0 387 26" preserveAspectRatio="none" aria-hidden="true"><path d="M0 12 C50 4 90 20 140 10 S210 2 250 14 S320 20 360 8 L387 12 L387 26 L0 26Z" fill="#404042"/></svg>
    <div class="principle principle--base">
      <h3>COORDINATE all activities:</h3>
      <p class="summary">Successful recovery recognises, supports and builds on individual, community and organisational capacity and resilience. Recovery should:</p>
      <ul class="checklist">
        <li>Assess capability and capacity requirements before, during and after a disaster;</li>
        <li>Support the development of self-reliance, preparation and disaster mitigation;</li>
        <li>Quickly identify and mobilise community skills, strengths and resources;</li>
        <li>Develop networks and partnerships to strengthen capacity, capability and resilience;</li>
        <li>Support training and knowledge sharing to sustain recovery capability across staff, volunteers and the community;</li>
        <li>Ensure mental health and wellbeing supports are available for staff, volunteers and communities involved in disaster recovery;</li>
        <li>Recognise that resources can be provided by a range of partners and from community networks;</li>
        <li>Acknowledge that existing resources may be stretched, and that additional resources may be required;</li>
        <li>Understand that additional resources may only be available for a limited period, and that sustainability may need to be addressed;</li>
        <li>Understand when and how to step back, while continuing to support individuals and the community as a whole to be more self-sufficient when they are ready; and</li>
        <li>Monitor, evaluate and capture learning to strengthen future recovery and preparedness, and build resilience.</li>
      </ul>
    </div>
  </article>
</section>

</body>
</html>
```